Uncoded front page web design for wedding and event planning company

Hi.

I am launching a wedding and event planning company called Silver Fern Gatherings and need a professional and appealing web design.

So, let me explain my company. I am based in Swindon in Wiltshire but the company will plan weddings and events in Oxfordshire, Wiltshire, Berkshire and London.

We will plan weddings, birthdays, conferences, product launches, fashion shows and conventions but the main focus of the website at this stage should be the weddings with all the other occasions being covered under a single 'events' heading.

My contact details for the website should be:
Maureen Pollard
maureen@silverferngatherings.co.uk
01632 960571 / 07700 900384

I'd like the website to feel clean, bright and elegant and be set against a white or off-white background. My logo is purple and I'd therefore like some purple incorporated into the design although feel free to use a more muted purple as my one might be a little bright? I'm also considering whether it would look nice paired with a little of the colour gold - maybe as a font colour in places?? I'll leave you to figure that one out as your design eye will be better than mine but for your reference below is my purple colour and my suggested gold one....

My purple colour is Pantone 2592 C but feel free to use others
My suggested gold I'm looking at is Pantone 14-1041 TCX

I would like to incorporate a Facebook feed in the front page if possible, if it looks right. I'd also like to include a variety of pictures as well so I've included a few in a Dropbox folder which is linked below. Please don't feel obliged to use them all by any means (there's loads!) but you've got a few there to play with. If you find any other royalty free images you'd rather use please go ahead but on the understanding I can have them afterwards!

My logo can be retrieved via this Dropbox link...
You'll notice there are 2 styles of placement. Please feel free to use either to fit in with your design...
https://www.filebarrow.net/sh/kq7pw2mzt4xn8bc/BBBLqr5hoPnvtc6S41MkwvaHb?dl=0

The wedding images I have are in this Dropbox folder...
https://www.filebarrow.net/sh/r8ym3vk6fa2lp9q/BBB4dzrTy8kW5nh63LxPeqjsc?dl=0

Other than that, it's over to you.... I can't wait to receive your designs :-)

Ooh....finally just to say, as I receive designs in I think I'll notice aspects that I like and don't like and if I feel they'll be useful for other designers, I'll update my brief below. Thanks

BRIEF UPDATE:
Someone asked if I had a tag-line. Could you use "Creating exquisite occasions today for amazing memories tomorrow"

I realise I hadn't explained what I'd like included on my home page so here's some notes to consider....

A welcome to section for me to start narrative about us and our services which has a button that links to our 'about us' page and 'services' page for further information.

A section that nicely illustrates what services we offer whether that be with icons or pictures.

A section with some photos in that would link to our gallery

A section that shows some customer reviews and blog entries that would link to my reviews page and blog to read more.

And finally a contact us section with my details, social media links and site map.

***
I also need to draw attention to where in the UK my services cover. I was therefore thinking perhaps we could use a picture to demonstrate this where it highlights Wiltshire, Oxfordshire, Berkshire and London on a map thereby demonstrating our areas covered. I have found several English county maps when searching on Google but I'm not sure how to highlight the areas I cover (or dull out the areas I don't) so if you have any ideas on this, I'd really like it incorporated. Thanks. (by the way, for those of you not familiar with English counties, the ones I cover are often abbreviated to Wilts, Oxon, Berks, London, so if you find a suitable map with those names on rather than the full names, you'll know what they are!)

I've found an image of the county map which might work well. I was wondering whether we might somehow grey out the counties I don't cover and just keep the ones I do as mentioned above and then crop it into perhaps a shadowed circle? I've attached a screenshot to the brief.
Updates

I've decided on the tag-line "Creating exquisite occasions today for amazing memories tomorrow" so if that could be included somewhere that would be great. I also need to draw attention to where in the UK my services cover. I was therefore thinking perhaps we could use a picture to demonstrate this where it highlights Wiltshire, Oxfordshire, Berkshire and London on a map thereby demonstrating our areas covered. I have found several English county maps when searching on Google but I'm not sure how to highlight the areas I cover (or dull out the areas I don't) so if you have any ideas on this, I'd really like it incorporated. Thanks. Added Wednesday, June 24, 2015

Target Market(s)

Predominately women aged 25-55

Industry/Entity Type

Wedding Planner

Number of Pages Required

1 page

Font styles to use
Sans Serif
Script

Requirements
Nice to have
• I'd like to see how the colour theme of purple and perhaps a little gold (maybe as a font colour) look against a white background. I've mentioned the Pantone colours in the brief above.
• I've attached a screenshot of a webpage with gold writing in and fonts that I like. Perhaps it could give you inspiration?
Should not have
• I really don't like the font SCRIPTINA so please done use that.

```html
<!DOCTYPE html>
<html lang="en">
<head>
<meta charset="utf-8">
<title>Silver Fern Gatherings – Weddings &amp; Events</title>
<link rel="stylesheet" href="https://fonts.googleapis.com/css2?family=Open+Sans:ital,wght@0,400;0,700;1,400&family=Raleway:wght@300;400;500&family=Roboto:wght@400;500&family=Dancing+Script:wght@500&display=swap">
<style>
  :root {
    --purple: #a02fa6;
    --purple-deep: #7e2584;
    --purple-band: #9b3aa0;
    --button: #b53bb0;
    --ink: #1c1a1f;
    --nav-ink: #2d2a30;
    --muted: #a9a3ad;
    --label: #8f8a93;
    --panel: rgba(255, 255, 255, 0.93);
    --white: #ffffff;
  }
  * { margin: 0; padding: 0; box-sizing: border-box; }
  html, body { width: 1200px; height: 925px; overflow: hidden; background: var(--white); }
  body { position: relative; font-family: "Open Sans", Arial, sans-serif; }

  .hero-photo {
    position: absolute; left: 0; top: 0; width: 1200px; height: 870px;
    background:
      radial-gradient(ellipse 250px 190px at 860px 450px, #fbfaf3 0%, #f6f3e6 45%, rgba(240, 238, 225, 0) 100%),
      radial-gradient(ellipse 330px 260px at 830px 470px, rgba(226, 232, 205, 0.85) 0%, rgba(226, 232, 205, 0) 100%),
      radial-gradient(ellipse 95px 260px at 410px 420px, rgba(238, 234, 242, 0.9) 0%, rgba(238, 234, 242, 0) 100%),
      radial-gradient(ellipse 150px 330px at 420px 420px, rgba(118, 102, 138, 0.75) 0%, rgba(118, 102, 138, 0) 100%),
      radial-gradient(ellipse 700px 150px at 560px 690px, rgba(140, 122, 168, 0.9) 0%, rgba(140, 122, 168, 0) 100%),
      radial-gradient(ellipse 320px 520px at 120px 330px, rgba(160, 150, 178, 0.85) 0%, rgba(160, 150, 178, 0) 100%),
      linear-gradient(90deg, #b4abc2 0%, #c6bfd2 30%, #dcd8e6 55%, #edecf4 75%, #f5f5fa 100%);
  }
  .hero-photo::after {
    content: ""; position: absolute; left: 0; right: 0; top: 620px; height: 250px;
    background: linear-gradient(180deg, rgba(160, 140, 185, 0) 0%, rgba(170, 148, 192, 0.45) 40%, rgba(228, 196, 206, 0.55) 72%, #ffffff 100%);
  }

  .site-header {
    position: absolute; left: 83px; top: 0; width: 1040px; height: 169px;
    background: var(--panel); text-align: center;
  }
  .header-band {
    height: 16px;
    background: linear-gradient(90deg, var(--purple-deep), var(--purple-band) 50%, #b04fa8);
  }
  .brand {
    display: flex; align-items: center; justify-content: center; gap: 12px;
    margin-top: 30px; height: 48px;
  }
  .brand-dot { width: 36px; height: 36px; border-radius: 50%; background: var(--purple); }
  .brand-name {
    font-family: "Raleway", Arial, sans-serif; font-weight: 400; font-size: 30px;
    color: var(--purple); letter-spacing: 1px;
  }
  .tagline {
    font-family: "Dancing Script", cursive; font-size: 16px; color: var(--purple);
    margin-top: 12px; letter-spacing: 0.3px;
  }
  .main-nav {
    display: flex; justify-content: center; margin-top: 14px;
    font-size: 13.5px; color: var(--nav-ink);
  }
  .main-nav a { color: inherit; text-decoration: none; padding: 0 14px; border-left: 1px solid #9a959e; line-height: 15px; }
  .main-nav a:first-child { border-left: 0; }
  .main-nav a.is-current { color: var(--purple); }

  .hero-copy { position: absolute; left: 106px; top: 393px; width: 420px; }
  .hero-lead {
    font-style: italic; font-size: 19.5px; line-height: 25px; color: var(--ink); letter-spacing: -0.4px;
  }
  .btn-gallery {
    display: inline-flex; align-items: center; gap: 16px;
    margin-top: 20px; width: 205px; height: 37px; padding-left: 23px;
    background: var(--button); color: var(--white); text-decoration: none;
    font-weight: 700; font-size: 16px; letter-spacing: 1.4px; border-radius: 2px;
  }

  .welcome {
    position: absolute; left: 73px; top: 748px; width: 1045px; height: 200px;
    background: var(--white); text-align: center;
  }
  .welcome-kicker {
    margin-top: 38px; font-family: "Roboto", Arial, sans-serif; font-size: 11.5px;
    letter-spacing: 1.3px; color: var(--label);
  }
  .welcome-title {
    margin-top: 7px; font-family: "Raleway", Arial, sans-serif; font-weight: 300;
    font-size: 37px; color: var(--purple); letter-spacing: 0.5px;
  }
  .welcome-text {
    width: 780px; margin: 12px auto 0; font-family: "Roboto", Arial, sans-serif;
    font-size: 12px; line-height: 22px; color: var(--muted);
  }
</style>
</head>
<body>
  <div class="hero-photo" role="img" aria-label="Soft-focus photo of a bride and groom kissing behind a white lily and rose bouquet resting on pale lavender rocks"></div>

  <header class="site-header">
    <div class="header-band"></div>
    <div class="brand">
      <span class="brand-dot"></span>
      <span class="brand-name">Silver Fern Gatherings</span>
    </div>
    <p class="tagline">Creating exquisite occasions today for amazing memories tomorrow</p>
    <nav class="main-nav">
      <a class="is-current" href="#">Home</a>
      <a href="#">Wedding Events</a>
      <a href="#">Our Services</a>
      <a href="#">Events</a>
      <a href="#">Contact Us</a>
    </nav>
  </header>

  <section class="hero-copy">
    <p class="hero-lead">We organize weddings, birthdays, conferences, product launches, fashion shows and conventions...</p>
    <a class="btn-gallery" href="#">VIEW GALLERY
      <svg width="16" height="16" viewBox="0 0 16 16" aria-hidden="true">
        <circle cx="8" cy="8" r="6.5" fill="none" stroke="#fff" stroke-width="1.8"/>
        <path d="M4.8 8h5.6M8 5.4 10.6 8 8 10.6" fill="none" stroke="#fff" stroke-width="1.8" stroke-linecap="round" stroke-linejoin="round"/>
      </svg>
    </a>
  </section>

  <section class="welcome">
    <p class="welcome-kicker">VESTI BULUM COMMODO VOLUTPAT</p>
    <h1 class="welcome-title">WE KNOW HOW TO DO EVENTS</h1>
    <p class="welcome-text">Etiam ullamcorper. Suspendisse a pellentesque dui, non felis. Maecenas malesuada elit lectus felis, malesuada ultricies. Curabitur et ligula. Ut molestie a, ultricies porta urna. Vestibulum commodo volutpat a, convallis ac, laoreet enim. Phasellus fermentum in, dolor. Pellentesque facilisis malesuada elit lectus felis ifend justo vel bibendum sapien.</p>
  </section>
</body>
</html>
```